Marlowe Dance Academy- Stationery
Stationery-biz card/letterhead/envelope/postcard
Use same font as used in my logo
Dana Velthorpe
Owner/Artistic Director
Birchmont Plaza 2174 Birchmont Lane Fernbrook, WI 44871
info@mdadance.example
www.mdadance.example
Tagline: Moving Gracefully...Dreaming Boldly...Becoming Artists
Looking for creativity from designer

```html
<!DOCTYPE html>
<html lang="en">
<head>
<meta charset="utf-8">
<title>Marlowe Dance Academy – Stationery</title>
<link href="https://fonts.googleapis.com/css2?family=Raleway:wght@400;600&display=swap" rel="stylesheet">
<style>
  :root{
    --backdrop:#3b3c3d;
    --teal-dark:#2c4a4c;
    --teal:#3fb7bd;
    --teal-soft:#cdeced;
    --paper:#ffffff;
    --ink:#3a5456;
    --muted:#8aa0a1;
    --line:#e3ecec;
  }
  *{margin:0;padding:0;box-sizing:border-box}
  html,body{width:1200px;height:271px;overflow:hidden;background:var(--backdrop)}
  body{font-family:"Raleway",sans-serif;color:var(--ink);position:relative}
  .piece{position:absolute;box-shadow:0 2px 6px rgba(0,0,0,.45);overflow:hidden}
  .brand{font-weight:600;color:var(--teal);line-height:1.15;text-align:center;display:flex;flex-direction:column;align-items:center;gap:2px;white-space:nowrap}
  .brand .dot{width:6px;height:6px;border-radius:50%;background:var(--teal)}
  .tiny{font-size:4px;line-height:1.5;white-space:nowrap}

  /* vertical business cards */
  .card-vertical{width:44px;height:104px;top:72px;background:var(--teal-dark);
    display:flex;flex-direction:column;align-items:center;justify-content:center;gap:5px;padding:4px}
  .card-vertical.front{left:12px}
  .card-vertical.back{left:60px}
  .card-vertical .brand{font-size:6px;color:var(--paper)}
  .card-vertical .tiny{font-size:3.2px;color:var(--teal-soft);text-align:center}
  .card-vertical .band{width:100%;height:2px;background:var(--teal)}

  /* brand showcase */
  .brand-showcase{position:absolute;left:112px;top:72px;width:160px;text-align:center}
  .brand-showcase .brand{font-size:11px;font-weight:400}
  .brand-showcase .tagline{font-size:4px;color:var(--teal-soft);margin-top:5px;white-space:nowrap}

  /* horizontal business cards */
  .card-horizontal{width:84px;height:36px;padding:4px 5px;display:flex;flex-direction:column;justify-content:space-between}
  .card-horizontal.light{background:var(--paper)}
  .card-horizontal.colour{background:var(--teal);color:var(--paper)}
  .card-horizontal .name{font-size:5px;font-weight:600}
  .card-horizontal .role{font-size:3.2px;color:var(--muted)}
  .card-horizontal.colour .role{color:var(--teal-soft)}
  .card-horizontal .tiny{font-size:3.2px;color:var(--muted)}
  .card-horizontal.colour .tiny{color:var(--teal-soft)}
  .card-horizontal .brand{font-size:5px}
  .card-horizontal.colour .brand{color:var(--paper)}
  .card-horizontal.colour .brand .dot{background:var(--paper)}
  .card-horizontal.centred{justify-content:center}

  /* letterheads */
  .letterhead{width:180px;height:238px;top:18px;background:var(--paper);padding:10px 12px 0;display:flex;flex-direction:column}
  .letterhead .brand{font-size:7px}
  .letterhead .rule{height:1px;background:var(--teal);margin:5px 0 4px}
  .letterhead .tiny{font-size:3.5px;color:var(--muted);text-align:center}
  .letterhead .body-lines{flex:1;display:flex;flex-direction:column;gap:5px;margin-top:12px}
  .letterhead .body-lines span{height:1px;background:var(--line);display:block}
  .letterhead .flourish{position:absolute;left:24px;right:24px;bottom:30px;height:70px;
    background:radial-gradient(ellipse at 50% 60%,rgba(63,183,189,.2),rgba(63,183,189,0) 70%)}
  .letterhead .footer{position:absolute;left:0;right:0;bottom:0;height:8px;background:var(--teal-dark);
    color:var(--teal-soft);font-size:3.5px;display:flex;align-items:center;justify-content:center;white-space:nowrap}

  /* comp slips */
  .slip{width:190px;height:38px;left:762px;background:var(--paper);padding:5px 7px;display:flex;justify-content:space-between;align-items:flex-start}
  .slip .brand{font-size:6px}
  .slip .tiny{color:var(--muted);text-align:right}
  .slip.banded{border-bottom:3px solid var(--teal)}

  /* envelopes */
  .envelope{width:200px;height:80px;background:var(--paper)}
  .envelope .flap{position:absolute;inset:0;width:100%;height:100%}
  .envelope .return{position:absolute;left:10px;top:32px}
  .envelope .return .brand{font-size:6px}
  .envelope .return .tiny{color:var(--muted)}
</style>
</head>
<body>

  <!-- vertical cards -->
  <div class="piece card-vertical front">
    <div class="brand"><span class="dot"></span>Marlowe<br>Dance<br>Academy</div>
  </div>
  <div class="piece card-vertical back">
    <div class="band"></div>
    <div class="tiny">Dana Velthorpe<br>Owner/Artistic Director<br><br>Birchmont Plaza<br>2174 Birchmont Lane<br>Fernbrook, WI 44871<br>info@mdadance.example<br>www.mdadance.example</div>
    <div class="band"></div>
  </div>

  <!-- brand showcase -->
  <div class="brand-showcase">
    <div class="brand"><span class="dot"></span>Marlowe Dance Academy</div>
    <div class="tagline">Moving Gracefully...Dreaming Boldly...Becoming Artists</div>
  </div>

  <!-- horizontal cards -->
  <div class="piece card-horizontal light" style="left:12px;top:186px">
    <div><div class="name">Dana Velthorpe</div><div class="role">Owner/Artistic Director</div></div>
    <div class="tiny">2174 Birchmont Lane · Fernbrook, WI 44871</div>
  </div>
  <div class="piece card-horizontal colour centred" style="left:102px;top:186px">
    <div class="brand"><span class="dot"></span>Marlowe Dance Academy</div>
  </div>
  <div class="piece card-horizontal light centred" style="left:192px;top:186px">
    <div class="brand"><span class="dot"></span>Marlowe Dance Academy</div>
  </div>
  <div class="piece card-horizontal colour" style="left:12px;top:228px">
    <div><div class="name">Dana Velthorpe</div><div class="role">Owner/Artistic Director</div></div>
    <div class="tiny">info@mdadance.example</div>
  </div>
  <div class="piece card-horizontal light" style="left:102px;top:228px">
    <div class="tiny">Birchmont Plaza</div>
    <div class="tiny">www.mdadance.example</div>
  </div>
  <div class="piece card-horizontal colour centred" style="left:192px;top:228px">
    <div class="brand"><span class="dot"></span>Marlowe Dance Academy</div>
  </div>

  <!-- letterheads -->
  <div class="piece letterhead" style="left:322px">
    <div class="brand"><span class="dot"></span>Marlowe Dance Academy</div>
    <div class="rule"></div>
    <div class="tiny">Birchmont Plaza · 2174 Birchmont Lane · Fernbrook, WI 44871</div>
    <div class="body-lines"><span></span><span></span><span style="width:80%"></span><span style="width:60%"></span></div>
    <div class="flourish" role="img" aria-label="Flowing ribbon flourish decoration"></div>
    <div class="footer">Moving Gracefully...Dreaming Boldly...Becoming Artists</div>
  </div>
  <div class="piece letterhead" style="left:568px">
    <div class="brand"><span class="dot"></span>Marlowe Dance Academy</div>
    <div class="rule"></div>
    <div class="tiny">info@mdadance.example · www.mdadance.example</div>
    <div class="body-lines"></div>
    <div class="flourish" role="img" aria-label="Flowing ribbon flourish decoration"></div>
    <div class="footer">Moving Gracefully...Dreaming Boldly...Becoming Artists</div>
  </div>

  <!-- comp slips -->
  <div class="piece slip" style="top:48px">
    <div class="brand"><span class="dot"></span>Marlowe Dance Academy</div>
    <div class="tiny">2174 Birchmont Lane<br>Fernbrook, WI 44871</div>
  </div>
  <div class="piece slip banded" style="top:94px">
    <div class="tiny" style="text-align:left">With compliments<br>Dana Velthorpe</div>
    <div class="tiny">www.mdadance.example</div>
  </div>

  <!-- envelopes -->
  <div class="piece envelope" style="left:972px;top:48px">
    <svg class="flap" viewBox="0 0 200 80" preserveAspectRatio="none" aria-hidden="true">
      <polygon points="0,0 200,0 100,32" fill="#3fb7bd"/>
    </svg>
    <div class="return"><div class="brand"><span class="dot"></span>Marlowe Dance Academy</div></div>
  </div>
  <div class="piece envelope" style="left:988px;top:142px">
    <svg class="flap" viewBox="0 0 200 80" preserveAspectRatio="none" aria-hidden="true">
      <polygon points="0,0 200,0 100,28" fill="#2c4a4c"/>
      <polyline points="0,80 100,40 200,80" fill="none" stroke="#e3ecec" stroke-width="1"/>
    </svg>
    <div class="return" style="top:36px"><div class="tiny">2174 Birchmont Lane<br>Fernbrook, WI 44871</div></div>
  </div>

</body>
</html>
```